Collaborative Business card design

I have a logo that I would like incorporate with my wife who is now a realtor as well.
Target Market(s)
Real Estate
Industry/Entity Type
Real Estate
Contact Information for Business Card
Names, Email accounts and phone numbers.. and Business info (required)
Font styles to use
Script
Colors
A7469A
B969AE
D3A5CF
EDDBEB
F8F0F9
Requirements
Must have
- Both Pictures and the logo from the previous business card

```html
<!DOCTYPE html>
<html lang="en">
<head>
<meta charset="utf-8">
<title>Harlan Reed Real Estate – Business Cards</title>
<link rel="stylesheet" href="https://fonts.googleapis.com/css2?family=Cinzel:wght@600&family=PT+Sans:wght@400;700&display=swap">
<style>
  :root {
    --backdrop: #2a2a2c;
    --card: #f7f7f6;
    --navy: #2d1c86;
    --red: #d2280e;
    --plum: #7a2b5f;
    --text-grey: #4a4a4f;
    --white: #ffffff;
  }
  * { box-sizing: border-box; margin: 0; padding: 0; }
  html, body {
    width: 1200px; height: 874px; overflow: hidden;
    background: var(--backdrop);
  }
  .canvas {
    position: relative; width: 1200px; height: 874px;
    display: flex; flex-direction: column; align-items: center;
    justify-content: center; gap: 40px;
  }
  .card {
    position: relative; width: 640px; height: 366px;
    background: var(--card); overflow: hidden;
    box-shadow: 0 14px 30px rgba(0,0,0,.45);
  }
  .brand {
    position: absolute; display: flex; flex-direction: column; align-items: center;
  }
  .brand-square {
    width: 64px; height: 64px; background: var(--navy); margin-bottom: 10px;
  }
  .wordmark {
    font-family: "Cinzel", serif; font-weight: 600;
    color: var(--navy); text-align: center; line-height: 1.05;
  }
  .wordmark .name { display: block; font-size: 40px; letter-spacing: .5px; }
  .wordmark .trade { display: block; font-size: 17px; letter-spacing: 8px; margin-top: 6px; }

  /* front */
  .card-front .brand { left: 0; right: 0; top: 84px; }
  .partner-badge {
    position: absolute; left: 36px; bottom: 40px;
    width: 60px; height: 60px; border-radius: 50%;
    border: 2px solid var(--plum);
  }
  .brokerage {
    position: absolute; right: 34px; bottom: 36px;
    font-family: "Cinzel", serif; font-weight: 600;
    color: var(--plum); font-size: 15px; line-height: 1.25; text-align: center;
  }

  /* back */
  .card-back .brand { left: 40px; top: 22px; width: 300px; }
  .card-back .brand-square { width: 50px; height: 50px; margin-bottom: 8px; }
  .card-back .wordmark .name { font-size: 32px; }
  .card-back .wordmark .trade { font-size: 14px; letter-spacing: 6px; }
  .contact {
    position: absolute; left: 44px; top: 178px;
    list-style: none; font-family: "PT Sans", sans-serif;
    font-size: 14px; color: var(--text-grey); line-height: 1.35;
  }
  .contact li { display: flex; align-items: flex-start; gap: 8px; }
  .contact svg { width: 12px; height: 12px; margin-top: 3px; flex: none; fill: var(--navy); }
  .services-band {
    position: absolute; left: 0; right: 0; bottom: 0; height: 58px;
    background: var(--red); display: flex; align-items: center;
    padding-left: 36px; font-family: "PT Sans", sans-serif; font-weight: 700;
    color: var(--white); font-size: 16px; letter-spacing: .4px;
  }
  .services-band .sep { margin: 0 10px; }
  .feature-area {
    position: absolute; left: 420px; top: 70px; right: 0; bottom: 0;
    background: linear-gradient(180deg, var(--navy) 0%, var(--navy) 55%, var(--red) 100%);
  }
  .portrait {
    position: absolute; width: 108px; height: 108px; border-radius: 50%;
    border: 3px solid var(--navy); box-shadow: 0 0 0 3px var(--white) inset;
  }
  .portrait-agent-one { left: 404px; top: 40px; background: radial-gradient(circle at 50% 45%, #8a5a44 0 38%, #1d1b20 60%, #9ab5d8 100%); }
  .portrait-agent-two { left: 518px; top: 92px; background: radial-gradient(circle at 50% 42%, #d9a58c 0 34%, #7a4a2e 52%, #151314 100%); }
</style>
</head>
<body>
<main class="canvas">
  <section class="card card-front" aria-label="Card front">
    <div class="brand">
      <div class="brand-square" aria-hidden="true"></div>
      <div class="wordmark">
        <span class="name">Harlan Reed</span>
        <span class="trade">Real Estate</span>
      </div>
    </div>
    <div class="partner-badge" aria-hidden="true"></div>
    <div class="brokerage">Summit Ridge<br>Homes &amp; Properties</div>
  </section>

  <section class="card card-back" aria-label="Card back">
    <div class="brand">
      <div class="brand-square" aria-hidden="true"></div>
      <div class="wordmark">
        <span class="name">Harlan Reed</span>
        <span class="trade">Real Estate</span>
      </div>
    </div>
    <ul class="contact">
      <li><svg viewBox="0 0 12 12"><path d="M6 0a4 4 0 0 0-4 4c0 3 4 8 4 8s4-5 4-8a4 4 0 0 0-4-4zm0 5.6A1.6 1.6 0 1 1 6 2.4a1.6 1.6 0 0 1 0 3.2z"/></svg><span>820 Canyon Rim Rd, Suite 12<br>Cedar Bluff Idaho 83000</span></li>
      <li><svg viewBox="0 0 12 12"><path d="M2.4 0l2 2.6-1.1 1.6a7 7 0 0 0 4.5 4.5l1.6-1.1L12 9.6 10.6 12C5 11.6.4 7 0 1.4z"/></svg><span>555-014-2287</span></li>
      <li><svg viewBox="0 0 12 12"><path d="M0 2h12v1.2L6 7 0 3.2zm0 2.6l6 3.8 6-3.8V10H0z"/></svg><span>harlan@summitridgehomes.com</span></li>
      <li><svg viewBox="0 0 12 12"><circle cx="6" cy="6" r="6"/></svg><span>summitridgehomes.com</span></li>
    </ul>
    <div class="services-band">RESIDENTIAL<span class="sep">|</span>COMMERCIAL<span class="sep">|</span>AGRICUTURAL</div>
    <div class="feature-area" role="img" aria-label="Large brand decoration area in navy and red"></div>
    <div class="portrait portrait-agent-one" role="img" aria-label="Portrait photo of the first agent"></div>
    <div class="portrait portrait-agent-two" role="img" aria-label="Portrait photo of the second agent"></div>
  </section>
</main>
</body>
</html>
```